Small Accounting Practice needs something creative

We need a business card design for a new small accounting practice based in Perth, Australia. The name of the practice is 'Kowra Ledger Partners Pty Ltd'. We providing Tax, Bookkeeping and Accounting services. Our target are individuals and small businesses. We want the design to be simply and creative. Also, we can the design can help us to gain people's trust.

Target Market(s)

Individuals and small businesses.

Industry/Entity Type

Accounting

Colors

Designer to choose colors to be used in the design.

```html
<!DOCTYPE html>
<html lang="en">
<head>
<meta charset="utf-8">
<title>Kowra Ledger Partners – Business Card</title>
<link href="https://fonts.googleapis.com/css2?family=Open+Sans:wght@400;600;700&display=swap" rel="stylesheet">
<style>
  :root {
    --blue-deep: #2450b8;
    --blue-bright: #1a8fdc;
    --gold: #f6b40e;
    --paper: #ffffff;
    --paper-shade: #e4e5e7;
    --ink: #2b2b2b;
    --brand: #1f6fc0;
    --backdrop: #eceef1;
  }
  * { margin: 0; padding: 0; box-sizing: border-box; }
  html, body { width: 1200px; height: 899px; overflow: hidden; }
  body {
    background: var(--backdrop);
    font-family: "Open Sans", Arial, sans-serif;
    position: relative;
  }
  .card {
    position: absolute;
    left: 290px;
    width: 620px;
    height: 354px;
    background: radial-gradient(ellipse at 55% 50%, var(--paper) 0%, var(--paper-shade) 100%);
    box-shadow: 0 6px 18px rgba(0,0,0,.18);
    overflow: hidden;
  }
  .card--back { top: 62px; }
  .card--front { top: 484px; }
  .card__band {
    position: absolute;
    left: 0; top: 0; right: 0;
    background: linear-gradient(90deg, var(--blue-deep) 0%, var(--blue-bright) 60%, var(--blue-deep) 100%);
    border-bottom: 6px solid var(--gold);
  }
  .card--back .card__band { height: 110px; }
  .card--front .card__band { height: 130px; }
  .brand {
    position: absolute;
    display: flex;
    align-items: center;
    gap: 12px;
  }
  .brand__dot {
    width: 46px; height: 46px;
    border-radius: 50%;
    background: var(--brand);
    flex: none;
  }
  .brand__name {
    color: var(--brand);
    font-weight: 600;
    font-size: 22px;
    line-height: 1.05;
  }
  .card--back .brand { left: 40px; top: 222px; }
  .card--front .brand { left: 56px; top: 226px; }
  .person { position: absolute; left: 26px; top: 46px; color: var(--paper); }
  .person__name { font-size: 22px; font-weight: 700; }
  .person__role { font-size: 16px; margin-top: 6px; }
  .address {
    position: absolute; left: 44px; top: 298px;
    font-size: 13px; color: var(--ink); line-height: 1.35;
  }
  .contacts {
    position: absolute; right: 24px; top: 168px;
    list-style: none; font-size: 13px; color: var(--ink);
  }
  .contacts li {
    display: flex; justify-content: flex-end; align-items: center;
    gap: 8px; height: 21px;
  }
  .contacts svg { width: 15px; height: 15px; flex: none; }
</style>
</head>
<body>

<section class="card card--back" aria-label="Card back">
  <div class="card__band" role="img" aria-label="Decorative blue band with gold edge"></div>
  <div class="brand">
    <span class="brand__dot"></span>
    <span class="brand__name">Kowra Ledger<br>Partners</span>
  </div>
</section>

<section class="card card--front" aria-label="Card front">
  <div class="card__band" role="img" aria-label="Decorative blue band with gold edge"></div>

  <div class="person">
    <p class="person__name">Mara Ellison</p>
    <p class="person__role">President</p>
  </div>

  <div class="brand">
    <span class="brand__dot"></span>
    <span class="brand__name">Kowra Ledger<br>Partners</span>
  </div>

  <p class="address">14 Hay Street, Suite 220<br>Perth WA 6000</p>

  <ul class="contacts">
    <li>08.6123.4470
      <svg viewBox="0 0 16 16"><path d="M2 6 Q8 1 14 6 L12 8 L10 6 H6 L4 8 Z M4 9 H12 V14 H4 Z" fill="var(--ink)"/></svg>
    </li>
    <li>08.6123.4471
      <svg viewBox="0 0 16 16"><rect x="4" y="1" width="8" height="14" rx="1.5" fill="none" stroke="var(--ink)" stroke-width="1.5"/><circle cx="8" cy="12.5" r="1" fill="var(--ink)"/></svg>
    </li>
    <li>hello@kowraledger.com.au
      <svg viewBox="0 0 16 16"><rect x="1" y="3" width="14" height="10" fill="var(--ink)"/><path d="M1 3 L8 9 L15 3" fill="none" stroke="var(--paper)" stroke-width="1.2"/></svg>
    </li>
    <li>www.kowraledger.com.au
      <svg viewBox="0 0 16 16"><circle cx="8" cy="8" r="6.5" fill="none" stroke="var(--ink)" stroke-width="1.4"/><ellipse cx="8" cy="8" rx="3" ry="6.5" fill="none" stroke="var(--ink)" stroke-width="1.1"/><path d="M1.5 8 H14.5" stroke="var(--ink)" stroke-width="1.1"/></svg>
    </li>
  </ul>
</section>

</body>
</html>
```